Wedding Decor and Entertianment business card

Company - We run a weddings and events company called Amber Fern, we provide most entertainment and decor services to our customers.

Initial idea is ....
A simple business card with logo on the front, this will be spot varnish. On a matt black background.
The reverse will be simple contact information.

But happy to try things outside of the box and would welcome some crazy ideas.

Target Market(s)

wedding couples - 21 - 40
High end wedding venues.

Industry/Entity Type

Wedding

Contact Information for Business Card

01742 918 263
amberfern.co.uk
rupert@amberfern.co.uk
or
eleanor@amberfern.co.uk

Requirements
Nice to have
• black matt background with spot varnish logo on the front.

```html
<!DOCTYPE html>
<html lang="en">
<head>
<meta charset="utf-8">
<title>Amber Fern — Business Card</title>
<link href="https://fonts.googleapis.com/css2?family=Jost:wght@400&family=Fira+Sans:wght@400&display=swap" rel="stylesheet">
<style>
  :root {
    --backdrop: #2b3134;
    --silver-light: #f4f4f4;
    --silver-mid: #d9d9da;
    --silver-dark: #bdbdbf;
    --ink: #1e1e1e;
    --matt-black: #050505;
    --paper-white: #f3f3f3;
    --faint-mark: rgba(0, 0, 0, 0.07);
  }
  * { margin: 0; padding: 0; box-sizing: border-box; }
  html, body {
    width: 1200px;
    height: 1120px;
    overflow: hidden;
    background: var(--backdrop);
  }
  .sheet {
    width: 1200px;
    height: 1120px;
    display: flex;
    flex-direction: column;
    align-items: center;
    justify-content: center;
    gap: 56px;
  }
  .card {
    position: relative;
    width: 840px;
    height: 480px;
    overflow: hidden;
    box-shadow: 0 10px 30px rgba(0, 0, 0, 0.35);
  }

  /* Contact side */
  .card--contact {
    background: linear-gradient(100deg, var(--silver-dark) 0%, var(--silver-mid) 22%, var(--silver-light) 50%, var(--silver-mid) 75%, var(--silver-dark) 100%);
  }
  .contact__decoration {
    position: absolute;
    right: -60px;
    top: 10px;
    width: 300px;
    height: 300px;
    border-radius: 50%;
    background: var(--faint-mark);
  }
  .contact__brand {
    position: absolute;
    left: 46px;
    top: 188px;
    display: flex;
    align-items: center;
    gap: 26px;
  }
  .brand-circle {
    width: 64px;
    height: 64px;
    border-radius: 50%;
    border: 6px solid var(--ink);
    flex: none;
  }
  .brand-name {
    font-family: 'Jost', sans-serif;
    font-weight: 400;
    font-size: 60px;
    letter-spacing: 0.32em;
    text-transform: uppercase;
    color: var(--ink);
    white-space: nowrap;
  }
  .contact__details {
    position: absolute;
    left: 0;
    right: 0;
    bottom: 28px;
    text-align: center;
    font-family: 'Fira Sans', sans-serif;
    font-size: 21px;
    line-height: 41px;
    color: var(--ink);
  }

  /* Logo side */
  .card--logo {
    background: var(--matt-black);
    display: flex;
    flex-direction: column;
    align-items: center;
    justify-content: center;
    gap: 48px;
  }
  .card--logo .brand-circle {
    width: 150px;
    height: 150px;
    border-width: 12px;
    border-color: var(--paper-white);
  }
  .card--logo .brand-name {
    font-size: 54px;
    color: var(--paper-white);
    padding-left: 0.32em;
  }
</style>
</head>
<body>
  <main class="sheet">
    <section class="card card--contact" aria-label="Business card, contact side">
      <div class="contact__decoration" aria-hidden="true"></div>
      <div class="contact__brand">
        <span class="brand-circle" aria-hidden="true"></span>
        <span class="brand-name">Amber Fern</span>
      </div>
      <div class="contact__details">
        <p>T: 01742 918 263 | W: amberfern.co.uk</p>
        <p>E: rupert@amberfern.co.uk | eleanor@amberfern.co.uk</p>
      </div>
    </section>

    <section class="card card--logo" aria-label="Business card, logo side">
      <span class="brand-circle" aria-hidden="true"></span>
      <span class="brand-name">Amber Fern</span>
    </section>
  </main>
</body>
</html>
```